Author needs cover design for health related book

I need the front cover designed for an upcoming book. I want a cover that will stand out when viewed in a thumbnail on sites such as Brellix. I'm open to the color scheme. The cover design should convey hopeful, uplifting energy, trust, and confidence. Nothing cute or frilly, please. The book is written for newly diagnosed cancer patients. The book title is: The Test Came Back, So Where Next? Subtitle: Steadily Facing Illness Through Dread, Confusion and Worry
Author: Marvina Tobbel
I'm not window shopping. I will definitely pick one of the submitted designs.
Target Market(s)
Newly diagnosed cancer patients
Industry/Entity Type
Health Care
Look and feel

```html
<!DOCTYPE html>
<html lang="en">
<head>
<meta charset="utf-8">
<title>The Test Came Back, So Where Next? — Book Cover</title>
<link rel="stylesheet" href="https://fonts.googleapis.com/css2?family=Tinos:wght@400;700&display=swap">
<style>
  :root {
    --page-bg: #e9e8e6;
    --ink: #111111;
    --accent-red: #d8151f;
    --tone-pink: #e9a0a6;
    --tone-peach: #f2b48e;
    --tone-gold: #f4c45e;
    --tone-dark: #1a110a;
    --figure-tone: #3b2219;
    --badge-ring: #fde8c4;
    --badge-fill: #050505;
    --badge-text: #ffffff;
    --gold-a: #f6e23c;
    --gold-b: #e6b322;
    --gold-c: #c99a16;
  }
  * { box-sizing: border-box; margin: 0; padding: 0; }
  html, body {
    width: 1022px; height: 1200px; overflow: hidden;
    background: var(--page-bg);
  }
  .cover {
    position: absolute; left: 111px; top: 0;
    width: 800px; height: 1200px; overflow: hidden;
    font-family: "Tinos", "Times New Roman", serif;
  }
  .cover-photo {
    position: absolute; left: 0; top: 0; width: 800px; height: 1091px;
    background: linear-gradient(to bottom,
      var(--tone-pink) 0%, var(--tone-peach) 40%, var(--tone-gold) 70%, var(--tone-dark) 100%);
  }
  .figure-area {
    position: absolute; left: 490px; top: 405px; width: 285px; height: 595px;
    border-radius: 12px;
    background: linear-gradient(to bottom, rgba(59,34,25,0.55), rgba(59,34,25,0.75));
  }
  .title {
    position: absolute; left: 0; right: 0; top: 68px;
    text-align: center; color: var(--ink);
    font-weight: 400; font-size: 82px; line-height: 99px;
    letter-spacing: 1px; text-transform: uppercase;
  }
  .title .title-accent { color: var(--accent-red); font-weight: 700; display: block; }
  .title-rule {
    position: absolute; left: 309px; top: 381px;
    width: 182px; height: 3px; background: var(--accent-red);
  }
  .subtitle-badge {
    position: absolute; left: 28px; top: 438px;
    width: 436px; height: 436px; border-radius: 50%;
    background: var(--badge-fill);
    box-shadow: 0 0 0 6px var(--badge-ring);
    display: flex; align-items: center; justify-content: center;
  }
  .subtitle {
    color: var(--badge-text); text-align: center;
    font-size: 35px; line-height: 44px; text-transform: uppercase;
  }
  .subtitle .subtitle-accent { color: var(--accent-red); font-weight: 700; }
  .author-band {
    position: absolute; left: 0; right: 0; bottom: 0; height: 109px;
    background: linear-gradient(to right, var(--gold-a) 0%, var(--gold-b) 55%, var(--gold-c) 100%);
    display: flex; align-items: center; justify-content: center;
  }
  .author {
    color: var(--ink); font-size: 60px; letter-spacing: 1px;
    text-transform: uppercase; font-weight: 400;
  }
</style>
</head>
<body>
  <main class="cover">
    <div class="cover-photo" role="img" aria-label="Photograph of a beach at sunset under a pink and golden sky, sea along the horizon"></div>
    <div class="figure-area" role="img" aria-label="Silhouette of a woman leaning back on the shore with arms outstretched"></div>

    <h1 class="title">
      The Test
      <span class="title-accent">Came Back,</span>
      So Where Next?
    </h1>
    <div class="title-rule"></div>

    <div class="subtitle-badge">
      <p class="subtitle">
        Steadily<br>
        <span class="subtitle-accent">Facing Illness</span><br>
        Through<br>
        Dread,<br>
        Confusion<br>
        and Worry
      </p>
    </div>

    <div class="author-band">
      <p class="author">Marvina Tobbel</p>
    </div>
  </main>
</body>
</html>
```